CSP 4 side flyer for industrial trace heating services

We are an electrical trace heating specialist wanting to expand our full EPC service to the CSP (concentrated solar power) industry. We need a flyer showing our USPs and capabilities so we can promote ourselves with the view to becoming an approved vendor to bid for work.
This flyer will be distributed to end user companys like Qasir Petrolux, Novar, TDM, Melvo etc along with contracting companies working on these sites whom would usually sub contract heat tracing work to companies like ours.
Much of our potential new business will be in the Middle East. However companies we work with are usually largest international firms.
The direct route to the supply chain first involves pre-qualification. A strong brand can help us ensure people take notice of us and help us through that process. We will also be making market visits and meeting contractors and end users on their sites so this new image will be followed through to our presentations and sub section of our website.

Target Market(s)

EPCs looking to outsource the CSP plant trace heating packages.

Industry/Entity Type

Power Generation

Colors
ec1f27

Requirements
Must have
• a sales focused edge.
• industrial feel
• high level appeal
Nice to have
• images.. we are short on the ground on royalty free CSP plant images

```html
<!DOCTYPE html>
<html lang="en">
<head>
<meta charset="utf-8">
<title>Kappa Therm – Trace Heating Spread</title>
<link href="https://fonts.googleapis.com/css2?family=Arimo:wght@400;700&display=swap" rel="stylesheet">
<style>
  :root{
    --brand-red:#ec1f27;
    --panel-top:#e9525b;
    --panel-bottom:#8c8a8d;
    --ink:#1a1a1a;
    --muted:#777777;
    --rule:#c9c9c9;
    --paper:#ffffff;
    --steel-light:#dfe7f0;
    --steel-mid:#8fa6bf;
    --steel-dark:#3f5670;
  }
  *{box-sizing:border-box;margin:0;padding:0}
  html,body{width:1200px;height:849px;overflow:hidden;background:var(--paper)}
  body{font-family:"Arimo",Arial,sans-serif;color:var(--ink);position:relative}
  .spread{position:relative;width:1200px;height:849px;overflow:hidden}
  .running-head{position:absolute;top:46px;font-size:10px;color:#333;letter-spacing:-.1px}
  .running-head.left{left:36px}
  .running-head.right{right:36px}
  .head-rule{position:absolute;top:61px;height:1px;background:var(--rule)}
  .head-rule.left{left:36px;width:276px}
  .head-rule.right{left:600px;width:564px}

  .photo{position:absolute}
  .photo-pipework{left:312px;top:0;width:288px;height:234px;
    background:linear-gradient(135deg,var(--steel-light) 0%,var(--steel-mid) 45%,var(--steel-dark) 100%)}
  .accent-square{position:absolute;left:289px;top:138px;width:47px;height:46px;
    background:linear-gradient(135deg,#ec6068,var(--brand-red));opacity:.9}
  .photo-solar{left:600px;top:234px;width:474px;height:268px;
    background:radial-gradient(circle at 72% 40%,#ffffff 0%,#e8eef5 12%,#a9b8c8 40%,#7d8a96 70%,#cfd9e4 100%)}
  .photo-plant{left:1024px;top:262px;width:140px;height:128px;
    background:linear-gradient(160deg,#7fb2de 0%,#2d5f95 55%,#10294a 100%)}
  .photo-field{left:36px;top:726px;width:528px;height:123px;
    background:linear-gradient(100deg,#d9503e 0%,#b76a5e 35%,#8d8b8c 70%,#7c7d80 100%)}

  .headline{position:absolute;left:34px;top:279px;width:320px;font-size:28.5px;line-height:27px;
    font-weight:700;letter-spacing:-.3px;text-transform:uppercase;color:#1c1c1c}
  .section-rule{position:absolute;left:36px;top:425px;width:528px;height:1px;background:var(--rule)}

  .block{position:absolute}
  .block h2{font-size:13.5px;font-weight:700;text-transform:uppercase;margin-bottom:8px;letter-spacing:-.1px}
  .block p{font-size:10.6px;line-height:14px;color:var(--muted);margin-bottom:11.5px;letter-spacing:-.05px}
  .block p.lead{color:var(--ink);font-weight:700}
  .design{left:36px;top:449px;width:252px}
  .materials{left:312px;top:449px;width:254px}
  .project{left:636px;top:86px;width:368px}

  .red-panel{position:absolute;left:600px;top:502px;width:600px;height:347px;
    background:linear-gradient(180deg,var(--panel-top) 0%,#c87a7c 50%,var(--panel-bottom) 100%)}
  .on-red h2{color:#fff}
  .on-red p{color:#fde6e6}
  .on-red p.lead{color:#fff}
  .installation{left:636px;top:530px;width:248px}
  .ownership{left:912px;top:530px;width:252px}
</style>
</head>
<body>
<main class="spread">
  <div class="running-head left">Dedicated Trace Heating Specialists</div>
  <div class="head-rule left"></div>
  <div class="running-head right">Dedicated Trace Heating Specialists</div>
  <div class="head-rule right"></div>

  <div class="photo photo-pipework" role="img" aria-label="Industrial plant pipework with insulated steel pipes and valves"></div>
  <div class="accent-square"></div>

  <section class="block project">
    <h2>Project Management:</h2>
    <p>Understanding of all contract interfaces, project deliverables and design and performance criteria demands high quality management and skilled supervision services.</p>
    <p class="lead">Kappa Therm offer proven site management and supervision expertise in Logistical Planning / Project Quality Systems / Health &amp; Safety / Engineering Standards / Design and Application.</p>
  </section>

  <div class="photo photo-solar" role="img" aria-label="Parabolic trough solar collector mirrors against a bright sky with the sun"></div>
  <div class="photo photo-plant" role="img" aria-label="Blue-lit industrial pipework and gauges"></div>

  <h1 class="headline">Key factors vital to ensuring long term performance and reliability include:</h1>
  <div class="section-rule"></div>

  <section class="block design">
    <h2>Design:</h2>
    <p>Extensive trace heating experience with detailed design and application knowledge paying particular respect to high temperature performance Mineral Insulated (MI) heating cables and units.</p>
    <p class="lead">Kappa Therm has proven expertise and a long successful track record in engineered system solutions for high and very high operating temperature trace heating.</p>
  </section>

  <section class="block materials">
    <h2>Materials:</h2>
    <p>Use of the highest quality MI cables and associated fully compatible ancillary equipment to conform to strict specifications and end user requirements.</p>
    <p>State of the art control systems to provide user information for simple and efficient long-term plant operation and ease of maintenance routines.</p>
    <p class="lead">Kappa Therm command conformance to our own strict in-house MI cable specifications and control systems provided by trusted 3rd party partners.</p>
    <p class="lead">Heating unit manufacture, controller hardware and software are produced to specific and exacting Kappa Therm technical standards under our direct control and quality conformance.</p>
  </section>

  <div class="photo photo-field" role="img" aria-label="Aerial view of a concentrated solar power plant field"></div>

  <div class="red-panel"></div>

  <section class="block on-red installation">
    <h2>Installation Services:</h2>
    <p>Fully trained, highly experienced and skilled installation labour is vital to ensuring trace heating design and performance criteria are met particularly with high operating temperature requirements.</p>
    <p class="lead">All Kappa Therm installers are directly employed with trace heating cumulative capability and experience of MI cable installations measured in many years on the job.</p>
    <p class="lead">Depending on specific project requirements, our supervisors / installers can be deployed in small teams to supplement / assist / support site based main contract labour if preferred. Full control and responsibility for work and installation standards is however always maintained by Kappa Therm.</p>
  </section>

  <section class="block on-red ownership">
    <h2>Cost of Ownership:</h2>
    <p>Ability to pro-actively work with and fully interpret client’s requirements to lower cost of ownership / increase product life cycle and simplify maintenance routines.</p>
    <p class="lead">Kappa Therm can demonstrate 40 years of specialist trace heating experience working with many major clients across the World delivering high performance, reliable engineered trace heating systems.</p>
    <p class="lead">Our expertise is regularly called on to assess and improve the operation and control of existing trace heating systems provided by others to deliver increased reliability and significant savings in power usage and maintenance costs.</p>
  </section>
</main>
</body>
</html>
```